International Rescue Training Company needs website redesign

Vantor 7 Global is a worldwide rescue training and accreditation company. We deliver water, rope, and medical training courses to emergency services, industry, government and outdoor adventure companies. We are currently looking to completely redesign our website. The main goals of this redesign are as follows:
1. Modernize the look of the website.
2. Make the website mobile compatible.
3. Focus on the international aspect of the business by making it less US focused than the current site. The new site will show us as an international brand. A separate (but similar) US site will be developed for the US market, similar in concept (but not design) to the one in place for our European office (www.vantor7europe.example).

The winning design should have:
1. Fully coded website
2. A modern, responsive design that would appeal to people in the emergency services, industrial and adventure recreation industries. Our courses are hands on, energetic, and fast paced and that should be conveyed in the design.
3. A navigation bar either at the top or side of the webpage (see attached document for page organization
4. 4 page designs: home page, template page, contact page, find a training provider page (interactive world map)

Still images and some video can be provided to aid in the design process.

Winning designer may be asked to consult on second US site.

Target Market(s)

Emergency Services (Fire, Police, Search and Rescue, Military)
Industrial Companies (Mines, Oil, Tower, etc)
Government (resource management, park rangers, road workers, etc)
Outdoor adventure companies and individuals (rafting, kayaking, highline, etc)

Industry/Entity Type

Training

Coding

Coded - Design and coding required

Number of Pages Required

4 page

Requirements
Must have
• 1. Fully coded
• 2. Mobile responsive design
• 3. Navigation bar
Nice to have
• -Dynamic images and videos
• -Interactive map or something similar so people can find a training provider in their region
Should not have
• Loud, bright, or pastel colors.

```html
<!DOCTYPE html>
<html lang="en">
<head>
<meta charset="utf-8">
<title>Vantor 7 Global — Rescue Training</title>
<link rel="stylesheet" href="https://fonts.googleapis.com/css2?family=Questrial&family=Oswald:wght@300;400&display=swap">
<style>
:root{
  --navy:#363b79;
  --navy-dark:#2f346c;
  --red:#a7363c;
  --red-light:#d55a5f;
  --red-dark:#ae3a40;
  --text:#444;
  --muted:#888;
  --line:#ddd;
  --white:#fff;
}
*{box-sizing:border-box;margin:0;padding:0}
html,body{width:1200px;height:2217px;overflow:hidden;background:var(--white)}
body{position:relative;font-family:"Questrial",sans-serif;color:var(--text)}
.abs{position:absolute}

/* header */
.topline{left:0;top:0;width:1200px;height:3px;background:var(--navy)}
.brand{left:100px;top:30px;display:flex;align-items:center;gap:10px;color:var(--navy);font-size:22px}
.brand .mark{width:22px;height:22px;border-radius:50%;background:var(--red)}
.contact-top{left:891px;font-size:13px;color:var(--navy);letter-spacing:.5px;display:flex;align-items:center;gap:6px}
.contact-top svg{width:12px;height:12px;fill:var(--navy)}

/* nav */
.nav{left:0;top:97px;width:1200px;height:58px;background:linear-gradient(var(--red-light),var(--red-dark))}
.nav a{position:absolute;top:0;height:58px;line-height:58px;color:var(--white);font-size:13px;text-decoration:none;letter-spacing:.5px;transform:translateX(-50%)}
.nav a.active{left:99px;width:176px;transform:none;text-align:center;background:var(--navy)}

/* hero */
.hero{left:0;top:155px;width:1200px;height:481px;background:linear-gradient(180deg,#9fb0bf 0%,#c3ccd4 45%,#d7b84a 70%,#c9a72e 85%,#b7b9b8 100%)}
.hero-caption{left:98px;top:384px;width:349px;height:175px;background:rgba(40,40,40,.55);color:var(--white);font-family:"Oswald",sans-serif;font-weight:300;font-size:22px;line-height:47px;padding:36px 0 0 17px;white-space:nowrap}
.dots{left:580px;top:607px;display:flex;gap:8px}
.dots span{width:8px;height:8px;background:var(--white)}
.dots span.on{background:var(--navy)}

/* section heads */
.section-title{left:0;width:1200px;text-align:center;font-size:31px;font-weight:400;letter-spacing:1px}
.section-title .a{color:var(--red)}
.section-title .b{color:var(--navy)}
.rule{left:525px;width:150px;height:1px;background:var(--line)}
.lead{left:0;width:1200px;text-align:center;font-size:13px;color:#333;line-height:23px}
.arrows{display:flex;gap:6px;color:#c9d3e3;font-size:20px}

/* cards */
.card{top:786px;width:321px;height:402px;border:1px solid #e2e2e2;background:var(--white)}
.card .photo{height:189px}
.card h3{position:absolute;left:20px;top:206px;font-weight:400;font-size:17px;color:var(--navy);letter-spacing:.5px}
.card p{position:absolute;left:20px;top:240px;width:285px;font-size:12.5px;line-height:21px;color:var(--muted)}
.card .more{position:absolute;left:20px;top:343px;width:100px;height:40px;border:1px solid var(--red);color:#333;font-size:14px;line-height:38px;text-align:center}
.card-shadow{top:1188px;width:321px;height:18px;background:radial-gradient(ellipse at 50% 0,rgba(0,0,0,.16),rgba(0,0,0,0) 70%)}

/* video carousel */
.video{background:#888;border:1px solid #bbb}
.video .frame{position:absolute;left:0;top:0;right:0}
.video .bar{position:absolute;left:0;right:0;bottom:0;background:linear-gradient(#fafafa,#d8d8d8);border-top:1px solid #aaa}
.side-arrow{color:#c7ced9;font-size:34px}

/* gallery */
.gallery{left:98px;top:1782px;width:1003px;height:160px;display:flex}
.gallery div{flex:1}

/* footer */
.footer{left:0;top:2023px;width:1200px;height:194px;background:var(--navy)}
.fcol{top:2053px;color:var(--white);font-size:11px;letter-spacing:.4px}
.fcol h4{font-weight:400;font-size:12px;margin-bottom:22px}
.fcol li{list-style:none;line-height:20.5px}
.subscribe{left:596px;top:2056px;display:flex}
.subscribe .field{width:192px;height:32px;background:var(--white);color:#bbb;font-size:11px;line-height:32px;padding-left:20px}
.subscribe .go{width:44px;height:32px;background:var(--red);color:var(--white);font-size:11px;line-height:32px;text-align:center}
.social{left:597px;top:2116px;display:flex;gap:10px}
.social span{width:17px;height:17px;border-radius:2px}
.copyright{left:0;top:2190px;width:1200px;text-align:center;color:var(--white);font-size:11px;letter-spacing:.4px}
</style>
</head>
<body>

<div class="abs topline"></div>

<header>
  <div class="abs brand"><span class="mark"></span>Vantor 7 Global</div>
  <div class="abs contact-top" style="top:23px">
    <svg viewBox="0 0 16 16"><path d="M3 1l3 3-2 2c1 2 3 4 5 5l2-2 3 3-2 3C6 15 1 10 1 3z"/></svg>: +44 (0) 1632 960418
  </div>
  <div class="abs contact-top" style="top:64px">
    <svg viewBox="0 0 16 16"><path d="M1 3h14v10H1z M1 3l7 6 7-6" fill="none" stroke="#363b79" stroke-width="2"/></svg>: INFO@VANTOR7EUROPE.EXAMPLE
  </div>
</header>

<nav class="abs nav">
  <a class="active" href="#">WHO WE ARE</a>
  <a href="#" style="left:353px">WHAT WE DO</a>
  <a href="#" style="left:525px">OUR TRAINING</a>
  <a href="#" style="left:692px">PROVIDERS</a>
  <a href="#" style="left:853px">CONTACT US</a>
  <a href="#" style="left:1007px">PORTALS</a>
</nav>

<section>
  <div class="abs hero" role="img" aria-label="Rescue team in red drysuits and helmets working from a yellow inflatable boat on icy water"></div>
  <div class="abs hero-caption">THE WORLD LEADER IN WATER &amp; ROPE<br>RESCUE EDUCATION SINCE 1979</div>
  <div class="abs dots"><span></span><span></span><span class="on"></span></div>
</section>

<section>
  <h2 class="abs section-title" style="top:666px"><span class="a">WHAT</span> <span class="b">WE DELIVER</span></h2>
  <div class="abs rule" style="top:714px"></div>
  <p class="abs lead" style="top:736px">Known for our dynamic curriculum and utilizing state of the art techniques.</p>
  <div class="abs arrows" style="left:1032px;top:716px">&lsaquo; &rsaquo;</div>

  <article class="abs card" style="left:100px">
    <div class="photo" role="img" aria-label="Industrial refinery towers at sunset" style="background:linear-gradient(#d9a148,#6f5a3f 70%,#3b3a3a)"></div>
    <h3>INDUSTRY</h3>
    <p>Ut enim ad minim veniam, quis nostrud exer-citation ullamco laboris nisi ut aliquip ex ea commodo consequat enim ad minim veniam, quis nostrud exercitation.</p>
    <div class="more">Read More</div>
  </article>
  <article class="abs card" style="left:440px">
    <div class="photo" role="img" aria-label="Divers performing a rescue in open water" style="background:linear-gradient(#3ea3b8,#1f6f86 60%,#2a4d5c)"></div>
    <h3>COURSE TYPE</h3>
    <p>Ut enim ad minim veniam, quis nostrud exer-citation ullamco laboris nisi ut aliquip ex ea commodo consequat enim ad minim veniam, quis nostrud exercitation ul.</p>
    <div class="more">Read More</div>
  </article>
  <article class="abs card" style="left:780px">
    <div class="photo" role="img" aria-label="Trainees in high-visibility vests during a first aid session" style="background:linear-gradient(#8a7a5e,#5d5240 60%,#8b6a3e)"></div>
    <h3>SPECIAL PROGRAMS</h3>
    <p>Ut enim ad minim veniam, quis nostrud exer-citation ullamco laboris nisi ut aliquip ex ea commodo consequat enim ad minim veniam, quis nostrud exercitation ullamc nisi</p>
    <div class="more">Read More</div>
  </article>
  <div class="abs card-shadow" style="left:100px"></div>
  <div class="abs card-shadow" style="left:440px"></div>
  <div class="abs card-shadow" style="left:780px"></div>
</section>

<section>
  <h2 class="abs section-title" style="top:1241px"><span class="a">WHAT</span> <span class="b">WE DO</span></h2>
  <div class="abs rule" style="top:1287px"></div>
  <p class="abs lead" style="top:1302px">Lorem Ipsum is simply dummy text of the printing and typesetting industry. Lorem Ipsum has been the industry's standard<br>dummy text ever since th and scrambled it to make a type specimen book.</p>

  <div class="abs side-arrow" style="left:118px;top:1482px">&lsaquo;</div>
  <div class="abs side-arrow" style="left:1060px;top:1482px">&rsaquo;</div>

  <div class="abs video" style="left:174px;top:1419px;width:198px;height:168px">
    <div class="frame" role="img" aria-label="Video still of a medical rescue drill" style="bottom:14px;background:linear-gradient(90deg,#c9c6bf,#9a8b73 50%,#b0b6bb)"></div>
    <svg class="bar" height="14" viewBox="0 0 198 14"><path d="M4 4h3v6H4zM10 4h2v6h-2zM14 4h2v6h-2z" fill="#333"/><rect x="24" y="6" width="170" height="2" fill="#888"/><circle cx="48" cy="7" r="5" fill="#fff" stroke="#777"/></svg>
  </div>
  <div class="abs video" style="left:832px;top:1419px;width:198px;height:168px">
    <div class="frame" role="img" aria-label="Video still of a rope rescue on a steel tower" style="bottom:14px;background:linear-gradient(#aebbc8,#7b8794 60%,#4f5257)"></div>
    <svg class="bar" height="14" viewBox="0 0 198 14"><rect x="4" y="6" width="160" height="2" fill="#888"/><path d="M172 3l5 4-5 4zM180 4h2v6h-2zM186 3l5 4-5 4z" fill="#333"/></svg>
  </div>
  <div class="abs video" style="left:370px;top:1386px;width:462px;height:229px;box-shadow:0 2px 6px rgba(0,0,0,.25)">
    <div class="frame" role="img" aria-label="Video still of a stretcher casualty rescue in woodland" style="bottom:20px;background:linear-gradient(#6b6a4f,#5a4f3a 50%,#6e5b46)"></div>
    <svg class="abs" style="left:206px;top:70px" width="50" height="50" viewBox="0 0 50 50"><rect width="50" height="50" rx="4" fill="rgba(120,120,120,.75)"/><path d="M19 14l16 11-16 11z" fill="#fff"/></svg>
    <svg class="bar" height="20" viewBox="0 0 462 20"><path d="M5 7h3v6H5zM9 5l4-3v16l-4-3zM22 5h3v10h-3zM28 5h3v10h-3z" fill="#222"/><rect x="40" y="9" width="370" height="3" rx="1" fill="#999"/><circle cx="62" cy="10" r="7" fill="#fff" stroke="#777"/><path d="M422 5l7 5-7 5zM432 5h2v10h-2zM440 5l7 5-7 5z" fill="#222"/></svg>
  </div>
</section>

<section>
  <h2 class="abs section-title" style="top:1694px"><span class="a">TRAINING</span> <span class="b">GALLERY</span></h2>
  <div class="abs rule" style="top:1740px"></div>
  <div class="abs arrows" style="left:1043px;top:1682px">&lsaquo; &rsaquo;</div>
  <div class="abs gallery">
    <div role="img" aria-label="Medics treating a casualty" style="background:linear-gradient(135deg,#c33a3a,#e6dcd6 60%,#8a8a8a)"></div>
    <div role="img" aria-label="Casualty wrapped in a foil blanket" style="background:linear-gradient(135deg,#b98a3a,#e0c36a 50%,#6b4f3a)"></div>
    <div role="img" aria-label="Firefighters in helmets at an incident" style="background:linear-gradient(135deg,#2a2a2a,#b22a2a 50%,#1e1e1e)"></div>
    <div role="img" aria-label="Rescuer in helmet using a radio" style="background:linear-gradient(135deg,#c9cfd3,#2c2f34 60%,#5b6066)"></div>
    <div role="img" aria-label="Rescuer in yellow helmet treating a casualty" style="background:linear-gradient(135deg,#d8c63a,#6b6b6b 50%,#b73030)"></div>
  </div>
</section>

<footer>
  <div class="abs footer"></div>
  <div class="abs fcol" style="left:100px">
    <h4>RESCUE TRAINING</h4>
    <ul><li>TRAINING COURSES</li><li>TRAINING PROVIDERS</li><li>INSTRUCTOR TRAINING</li><li>COURSE CALENDAR</li><li>CHECK VANTOR 7 QUALIFICATIONS</li></ul>
  </div>
  <div class="abs fcol" style="left:372px">
    <h4>RESOURCES</h4>
    <ul><li>STUDENT DOWNLOADS</li><li>ONLINE SHOP</li><li>BUY THE FIELD GUIDE</li><li>HANDBUCH FLIEßWASSERRETTER</li></ul>
  </div>
  <div class="abs subscribe"><div class="field">E MAIL</div><div class="go">GO</div></div>
  <div class="abs social">
    <span style="background:#4a6aa8"></span><span style="background:#3fa6d8"></span><span style="background:#2f78a8"></span><span style="background:#e58a2e"></span><span style="background:#d0453a"></span>
  </div>
  <div class="abs fcol" style="left:906px">
    <h4>CONTACT US</h4>
    <ul><li>THE OLD MILL</li><li>HARBOUR LANE</li><li>BRYNFORD LL99 4QT</li><li>UNITED KINGDOM</li></ul>
  </div>
  <p class="abs copyright">© 2015 VANTOR 7 EUROPE LTD ALL RIGHTS RESERVED</p>
</footer>

</body>
</html>
```